Spiritual journeyer, astrologer, Reiki master, underground music lover needs business card design

Initially I need a business card design (and possibly a logo for my new website). I offer astrological and energetic inquiry and guidance to clients in support of their life's evolutionary path. I combine an eclectic mix of methods with a focus on the mind body connection. I am a spiritual journeyer, astrologer, Reiki Master, certified personal trainer, soon to be black belt in Taekwondo (karate), and researcher into the benefits of music/sound vibrational therapy. And underground music lover :) The attached drawing is just something I drew freehand, it is symbolic of many things important to me. I wanted the figure to clearly be female. Her arms are open to catch the sky, the name of my new business is Noraweaver, and Nora is my daughter's name. This was just an idea I had, I'm open to suggestions. The photo is me with the planets in the sky as they were at the moment I was born (some years ago-LOL)

I have picked a final design. Thank you everyone for your time and effort.

Target Market(s)

Worldwide, what I do can be done in person or anywhere in the world via Skype

Industry/Entity Type

Professional Service

Contact Information for Business Card

Simple, unusual image with my business name and contact info

Font styles to use
Sans Serif

Requirements
Must have
• My website very clean, simple. Somehow combine biz name of Noraweaver with female figure catching/holding the starry sky? See my poor drawing I attached.
Nice to have
• Something that conveys all the unique, unusual, eclectic skills and capacities I have
Should not have
• Frilly, fancy, stuffy

```html
<!DOCTYPE html>
<html lang="en">
<head>
<meta charset="utf-8">
<title>Noraweaver — Business Card</title>
<link rel="stylesheet" href="https://fonts.googleapis.com/css2?family=Caveat+Brush&family=Cormorant+Garamond:wght@600;700&display=swap">
<style>
  :root {
    --page: #ffffff;
    --night-deep: #141427;
    --night-mid: #2b2a55;
    --night-glow: #4f4e8c;
    --flare: rgba(150, 170, 255, 0.55);
    --emblem-warm: rgba(214, 190, 150, 0.28);
    --emblem-shade: rgba(30, 28, 60, 0.55);
    --ink-light: #ffffff;
    --ink-gold: #e6cfa8;
    --ink-contact: #f1ece4;
  }
  html, body {
    margin: 0;
    padding: 0;
    width: 1200px;
    height: 1000px;
    overflow: hidden;
    background: var(--page);
  }
  .card {
    position: absolute;
    left: 39px;
    top: 189px;
    width: 1121px;
    height: 622px;
    overflow: hidden;
    font-family: "Cormorant Garamond", Georgia, serif;
  }
  .card__sky {
    position: absolute;
    inset: 0;
    background:
      linear-gradient(180deg, transparent 268px, var(--flare) 281px, transparent 294px),
      radial-gradient(circle 18px at 130px 310px, rgba(200, 200, 230, 0.18), transparent),
      radial-gradient(circle 22px at 410px 530px, rgba(200, 200, 230, 0.16), transparent),
      radial-gradient(circle 26px at 200px 110px, rgba(200, 200, 230, 0.14), transparent),
      radial-gradient(circle 20px at 215px 490px, rgba(200, 200, 230, 0.14), transparent),
      radial-gradient(ellipse 260px 120px at 390px 270px, rgba(170, 180, 255, 0.45), transparent 70%),
      radial-gradient(ellipse 700px 420px at 520px 320px, var(--night-glow), transparent 75%),
      radial-gradient(ellipse 900px 600px at 560px 340px, var(--night-mid), var(--night-deep));
  }
  .card__emblem {
    position: absolute;
    left: 574px;
    top: 96px;
    width: 410px;
    height: 410px;
    border-radius: 50%;
    background: radial-gradient(circle at 50% 48%, var(--emblem-shade) 0%, var(--emblem-warm) 62%, transparent 72%);
  }
  .card__wordmark {
    position: absolute;
    left: 164px;
    top: 196px;
    margin: 0;
    font-family: "Caveat Brush", "Brush Script MT", cursive;
    font-size: 136px;
    font-weight: 400;
    line-height: 1;
    color: var(--ink-light);
  }
  .card__tagline {
    position: absolute;
    left: 159px;
    top: 352px;
    margin: 0;
    font-size: 15px;
    font-weight: 700;
    letter-spacing: 3.6px;
    text-transform: uppercase;
    white-space: nowrap;
    color: var(--ink-gold);
  }
  .card__owner {
    position: absolute;
    left: 354px;
    top: 378px;
    margin: 0;
    font-family: "Caveat Brush", "Brush Script MT", cursive;
    font-size: 36px;
    font-weight: 400;
    color: var(--ink-gold);
    letter-spacing: 0.5px;
  }
  .card__contact {
    position: absolute;
    left: 0;
    right: 0;
    top: 560px;
    margin: 0;
    padding: 0 20px 0 0;
    list-style: none;
    display: flex;
    justify-content: center;
    gap: 28px;
    font-size: 22px;
    font-weight: 700;
    font-variant-numeric: lining-nums;
    color: var(--ink-contact);
    letter-spacing: 0.9px;
  }
</style>
</head>
<body>
  <section class="card">
    <div class="card__sky" role="img" aria-label="Deep violet night sky with soft bokeh star lights and a horizontal lens flare"></div>
    <div class="card__emblem" role="img" aria-label="Emblem area: female figure with arms open to the sky, set within a star and circle"></div>
    <h1 class="card__wordmark">Noraweaver</h1>
    <p class="card__tagline">Astrological and energetic guidance and inquiry</p>
    <p class="card__owner">Miriam Holt</p>
    <ul class="card__contact">
      <li>www.noraweaver.com</li>
      <li>hello@noraweaver.com</li>
      <li>(555)-214-0736</li>
    </ul>
  </section>
</body>
</html>
```